Hispanic Financial Counseling and Advocate Firm seeks business card design

Looking for a clean, professional business card design. This is a firm that specializes in providing financial education, coaching, and planning to the Hispanic community. The name of the company is Valemar, which means to prosper. We need a design that is clean, professional, and invokes trust, professionalism, but also welcoming. Our logo is a plant growing from a hand to give the messaging of of being in control of growing your financial future and security. Its part of a larger organization names Celesta Financial Group, who's logo is a tree with multi colored branches. We have the back of the card designed so we just need the front designed. the back is blue, so front needs to be a different background color, not blue.

Target Market(s)

Hispanic Community looking to better their future

Industry/Entity Type

financial services

Contact Information for Business Card

contact info: Anselmo Ibarra Jr, 951-555-0147, info@celestafinancialgroup.example. Celestafinancialgroup.example. tag line: Para un futuro mas seguro!

Requirements
Must have
• basics: logo, contact info.
Nice to have
• possibly incorporate the tree logo provided somehow
Should not have
• should not look like the back, needs to be different from the back provided.

```html
<!DOCTYPE html>
<html lang="es">
<head>
<meta charset="utf-8">
<title>Valemar – Tarjeta de presentación</title>
<link href="https://fonts.googleapis.com/css2?family=Nunito+Sans:wght@400;700;800&display=swap" rel="stylesheet">
<style>
  :root {
    --backdrop: #1d1f22;
    --card-white: #f3f3f2;
    --slate: #56647f;
    --slate-light: #63729a;
    --leaf-green: #6cb23f;
    --ink: #3f4b66;
    --text-light: #f4f6fa;
  }
  * { margin: 0; padding: 0; box-sizing: border-box; }
  html, body {
    width: 1200px; height: 900px; overflow: hidden;
    background: var(--backdrop);
    font-family: "Nunito Sans", sans-serif;
  }
  .canvas {
    width: 1200px; height: 900px;
    display: flex; align-items: center; justify-content: center;
  }
  .card {
    position: relative;
    width: 1000px; height: 572px;
    border-radius: 34px;
    overflow: hidden;
    background: var(--card-white);
    box-shadow: 0 18px 40px rgba(0,0,0,.45);
  }
  .card-wave { position: absolute; inset: 0; width: 100%; height: 100%; }
  .holder {
    position: absolute; left: 72px; top: 70px;
    border-left: 9px solid var(--leaf-green);
    padding-left: 22px;
    font-weight: 800; font-size: 30px; line-height: 1.12;
    letter-spacing: .5px; text-transform: uppercase;
  }
  .holder-first { color: var(--leaf-green); display: block; }
  .holder-last { color: var(--ink); display: block; }
  .contact-list {
    position: absolute; left: 72px; top: 300px;
    list-style: none;
    color: var(--text-light);
    font-size: 22px; line-height: 1.45;
  }
  .contact-list li { display: flex; align-items: center; gap: 12px; }
  .contact-icon { width: 18px; height: 18px; flex: none; }
  .brand {
    position: absolute; left: 600px; top: 250px;
    display: flex; flex-direction: column; align-items: flex-start;
  }
  .brand-row { display: flex; align-items: center; gap: 14px; }
  .brand-dot { width: 22px; height: 22px; border-radius: 50%; background: var(--leaf-green); }
  .brand-name {
    font-weight: 700; font-size: 64px; line-height: 1;
    color: var(--leaf-green); letter-spacing: -.5px;
  }
  .brand-sub {
    margin-top: 8px; margin-left: 36px;
    font-weight: 800; font-size: 15px; letter-spacing: 2px;
    color: var(--ink); text-transform: uppercase;
  }
  .tagline {
    position: absolute; right: 110px; bottom: 48px;
    color: var(--text-light);
    font-size: 24px; letter-spacing: .3px;
  }
</style>
</head>
<body>
<main class="canvas">
  <article class="card">
    <svg class="card-wave" viewBox="0 0 1000 572" preserveAspectRatio="none" aria-hidden="true">
      <path d="M0,215 C260,215 470,340 680,410 C820,456 920,470 1000,472 L1000,572 L0,572 Z" fill="var(--slate)"/>
      <path d="M0,196 C190,190 320,245 440,300" fill="none" stroke="var(--leaf-green)" stroke-width="7"/>
      <path d="M650,385 C780,440 900,455 1000,452" fill="none" stroke="var(--leaf-green)" stroke-width="6"/>
    </svg>

    <h1 class="holder">
      <span class="holder-first">Anselmo</span>
      <span class="holder-last">Ibarra Jr</span>
    </h1>

    <ul class="contact-list">
      <li>
        <svg class="contact-icon" viewBox="0 0 24 24"><path d="M6.6 10.8a15 15 0 0 0 6.6 6.6l2.2-2.2a1 1 0 0 1 1-.25 11.4 11.4 0 0 0 3.6.57 1 1 0 0 1 1 1V20a1 1 0 0 1-1 1A17 17 0 0 1 3 4a1 1 0 0 1 1-1h3.5a1 1 0 0 1 1 1c0 1.25.2 2.45.57 3.6a1 1 0 0 1-.25 1z" fill="var(--leaf-green)"/></svg>
        951-555-0147
      </li>
      <li>
        <svg class="contact-icon" viewBox="0 0 24 24"><rect x="2" y="5" width="20" height="14" rx="2" fill="var(--leaf-green)"/><path d="M3 6l9 7 9-7" fill="none" stroke="var(--slate)" stroke-width="2"/></svg>
        info@celestafinancialgroup.example
      </li>
      <li>
        <svg class="contact-icon" viewBox="0 0 24 24"><circle cx="12" cy="12" r="10" fill="var(--leaf-green)"/><path d="M2 12h20M12 2c3 3 3 17 0 20M12 2c-3 3-3 17 0 20" fill="none" stroke="var(--slate)" stroke-width="1.5"/></svg>
        www.celestafinancialgroup.example
      </li>
    </ul>

    <div class="brand">
      <div class="brand-row">
        <span class="brand-dot"></span>
        <span class="brand-name">Valemar</span>
      </div>
      <span class="brand-sub">Servicios Financieros</span>
    </div>

    <p class="tagline">Para un futuro mas seguro!</p>
  </article>
</main>
</body>
</html>
```